Wine label design for a family winery in Slovenia

We need new label design for our wines.
We are small family wine producers who focuses on good quality wine and loves to experiment, mixing tradition with new, more modern approaches. Our main product is ‘Teran’, red wine whose character is highly defined by terroir: more acidic, but rich body and very rich, dark colour (we say it's not red, but black). We also age a small portion of this Teran wine with wood, which we named 'Pelmik' (after one of our vineyards). From the same grapes as Teran we also produce a small quantity of Rose. And we also produce two white wine varieties: one is 'Sopa', cuvee of several different sorts of grapes. The other is 'Ostrena', Chardonnay wine, named after another of our vineyards. Aside from all that we also produce liquour (Teranov liker) made from Teran wine and a small quantity of other spirits (Grappa, various fruit liquors, a version of Blaustrummer, and ‘Travarica’ which is grappa infused with various herbs and spices).
Sopa, Rose and Teran are considered our 'basic' line, whereas 'Pelmik' and 'Ostrena' are considered to be a higher quality line. Rose sits somewhere between this two.
In time we'd like to renew all of our labels. But the priority and subject of this ‘’project’’ is to create the two for our top line, Pelmik and Ostrena and also for Rose.
For 'Pelmik' we already have a template label. The general idea behind it was play with letters and divide them along the label (PE LM IK). We found that we like the narrow, longer dimensions and that black label on black bottle, with letters that stand out due to colour or printing differences, work very well. But we're amateurs and the label is not finalized. We would ask you to do something on this basis, but please don't limit yourself only to this if you have a better idea.
For 'Ostrena' the label should be in the same style to imply the same higher quality line - colours can and probably should be reversed to the lighter side (so to imply that it’s a white wine). Also, for this wine we'll use the same dark slender bottles, like you see on the image.
Please keep in mind that we'll print smaller series (1000-2000 pcs), so it must be possible to print the labels for a sensible cost. Solutions like classical offset gold print that requires large series of 10.000 pcs, will not work. But we can look into any digital printing/lacquering options that offer similar effects. Anyway, we are not experts on this field, so your advice on printing techniques is also welcomed.
Also, a word on our emblem: the logo is also not finalized and we will also ask you to work on it. The logo is part of the ornament on the doors of our homestead and represents a ‘kolovrat’ (‘spinning wheel’ in English), an old Slavic symbol for the sun, representing eternal life and spinning of time. We'd like to use it, but right now it's badly digitalized. If you'll need any better photos of it, let me know.

Target Market(s)

30-60 yo, red wine lovers, appreciate local and speicality wines

Font styles to use
Sans Serif
Decorative

Requirements
Must have
• long, narrow label dimensions (see attached Pelmik)

```html
<!DOCTYPE html>
<html lang="sl">
<head>
<meta charset="utf-8">
<title>Wine label series – Pelmik, Ostrena, Rose</title>
<link rel="stylesheet" href="https://fonts.googleapis.com/css2?family=Oswald:wght@300;400;500&family=Montserrat:wght@600&display=swap">
<style>
  :root {
    --backdrop: #e1e1e1;
    --ink-black: #000000;
    --night: #2a0c11;
    --wine: #96151f;
    --wine-deep: #6b0a10;
    --rose-band: #300404;
    --paper: #ffffff;
  }
  * { margin: 0; padding: 0; box-sizing: border-box; }
  html, body { width: 1200px; height: 1149px; overflow: hidden; background: var(--backdrop); }
  .canvas { position: relative; width: 1200px; height: 1149px; }

  .label { position: absolute; top: 89px; width: 315px; height: 785px; overflow: hidden; }
  .label--pelmik { left: 89px; background: radial-gradient(ellipse 55% 60% at 50% 45%, #000 40%, var(--night) 100%); }
  .label--ostrena { left: 436px; background: var(--paper); }
  .label--rose { left: 791px; background: var(--wine); }

  .variety {
    position: absolute; left: 0; right: 0; text-align: center;
    font-family: "Montserrat", sans-serif; font-weight: 600;
    letter-spacing: 0.55em; text-indent: 0.55em;
  }
  .variety--top { top: 84px; font-size: 9px; }
  .variety--bottom { top: 390px; font-size: 13px; }

  .letter-grid {
    position: absolute; left: 26px; right: 26px; top: 118px;
    display: grid; grid-template-columns: repeat(4, 1fr); row-gap: 12px;
    font-family: "Oswald", sans-serif; font-weight: 300;
    font-size: 86px; line-height: 73px; text-align: center;
  }
  .letter-grid span { display: block; transform: scaleX(0.8); }

  .label--pelmik .variety { color: var(--paper); }
  .label--pelmik .lit { color: var(--paper); }
  .label--pelmik .shade { color: var(--wine-deep); }

  .label--ostrena .variety--top { color: var(--wine); }
  .label--ostrena .variety--bottom { color: var(--ink-black); }
  .label--ostrena .lit { color: var(--ink-black); }
  .label--ostrena .shade { color: var(--wine); }

  .letter-grid--rose {
    left: 102px; right: 102px; top: 76px;
    font-size: 42px; line-height: 33px; row-gap: 5px;
  }
  .letter-grid--rose span { transform: scaleX(0.6); }
  .label--rose .lit { color: var(--paper); }
  .label--rose .shade { color: var(--rose-band); }
  .label--rose .variety--bottom { top: 248px; color: var(--paper); }

  .band { position: absolute; left: 0; right: 0; top: 594px; height: 56px; background: var(--wine); }
  .label--rose .band { background: var(--rose-band); }
  .seal { position: absolute; left: 94px; top: 559px; width: 126px; height: 126px; }

  .winery {
    position: absolute; left: 0; right: 0; top: 712px; text-align: center;
    font-family: "Oswald", sans-serif; font-weight: 500; font-size: 22px; line-height: 1;
    letter-spacing: 0.12em; text-indent: 0.12em;
  }
  .label--pelmik .winery, .label--rose .winery { color: var(--paper); }
  .label--ostrena .winery { color: var(--wine); }

  .draft-note {
    position: absolute; left: 854px; top: 983px; width: 346px; height: 77px;
    background: #000; color: #fff; padding: 8px 10px;
    font-family: Arial, Helvetica, sans-serif; font-size: 17px; line-height: 20px;
  }
</style>
</head>
<body>
<main class="canvas">

  <section class="label label--pelmik">
    <p class="variety variety--top">DARK RED</p>
    <div class="letter-grid">
      <span class="lit">P</span><span class="lit">E</span><span class="shade">L</span><span class="shade">M</span>
      <span class="shade">E</span><span class="lit">L</span><span class="lit">M</span><span class="shade">I</span>
      <span class="shade">L</span><span class="shade">M</span><span class="lit">I</span><span class="lit">K</span>
    </div>
    <p class="variety variety--bottom">PELMIK</p>
    <div class="band"></div>
    <svg class="seal" viewBox="0 0 126 126"><circle cx="63" cy="63" r="61" fill="#96151f" stroke="#6b0a10" stroke-width="2"/></svg>
    <p class="winery">DOMAČIJA LOVRIN</p>
  </section>

  <section class="label label--ostrena">
    <p class="variety variety--top">CHARDONNAY</p>
    <div class="letter-grid">
      <span class="lit">O</span><span class="lit">S</span><span class="lit">T</span><span class="shade">R</span>
      <span class="shade">T</span><span class="lit">R</span><span class="lit">E</span><span class="shade">N</span>
      <span class="shade">R</span><span class="shade">E</span><span class="lit">N</span><span class="lit">A</span>
    </div>
    <p class="variety variety--bottom">OSTRENA</p>
    <div class="band"></div>
    <svg class="seal" viewBox="0 0 126 126"><circle cx="63" cy="63" r="61" fill="#96151f" stroke="#6b0a10" stroke-width="2"/></svg>
    <p class="winery">DOMAČIJA LOVRIN</p>
  </section>

  <section class="label label--rose">
    <div class="letter-grid letter-grid--rose">
      <span class="shade">O</span><span class="shade">S</span><span class="shade">E</span><span class="lit">R</span>
      <span class="shade">S</span><span class="shade">E</span><span class="shade">R</span><span class="lit">O</span>
      <span class="shade">E</span><span class="shade">R</span><span class="shade">O</span><span class="lit">S</span>
      <span class="lit">R</span><span class="lit">O</span><span class="lit">S</span><span class="lit">E</span>
    </div>
    <p class="variety variety--bottom">ROSE</p>
    <div class="band"></div>
    <svg class="seal" viewBox="0 0 126 126"><circle cx="63" cy="63" r="61" fill="#2e0404" stroke="#6b0a10" stroke-width="2"/></svg>
    <p class="winery">DOMAČIJA LOVRIN</p>
  </section>

  <div class="draft-note">DRAFT 1:<br>First version for proof of concept<br>for the 1st round of feedback</div>

</main>
</body>
</html>
```